Verdon Ridgeworks Ltd. - Refreshed business card challenge

A revised, refreshed business card design for my oil and gas company using my existing logo. Feel free to be as creative as you like!

Target Market(s)

bankers, lawyers

Industry/Entity Type

Oil And Gas Exploration

Contact Information for Business Card

See the "Must Haves" section

Font styles to use
Serif
Sans Serif

Colors

Designer to choose colors to be used in the design.

Requirements
Must have
• Existing business logo, name, title, email, phone number, business address
• Neil Hastow, CA, CPA
• Vice President Finance & Chief Financial Officer
• nhastow@verdonridgeworks.example
• office: (555)284-6071
• cell: (555)716-3342
• 840, 615 11 Street N.E.
• Calgary, AB
• X9Q 4K1
Should not have
• Should not be plain and boring.

```html
<!DOCTYPE html>
<html lang="en">
<head>
<meta charset="utf-8">
<title>Verdon Ridgeworks – Business Card</title>
<link href="https://fonts.googleapis.com/css2?family=Lato:wght@400;700;900&display=swap" rel="stylesheet">
<style>
  :root {
    --backdrop: #2a2a2a;
    --card-light: #eeeeee;
    --card-green: #064a2e;
    --card-green-soft: #1a5c3e;
    --brand-green: #0d4c33;
    --brand-brown: #6a2f12;
    --text-dark: #333333;
    --rule: #9a9a9a;
    --white: #ffffff;
  }
  html, body {
    margin: 0;
    padding: 0;
    width: 1200px;
    height: 1200px;
    overflow: hidden;
    background: var(--backdrop);
    font-family: "Lato", Arial, sans-serif;
  }
  .canvas {
    position: relative;
    width: 1200px;
    height: 1200px;
  }
  .card {
    position: absolute;
    top: 310px;
    height: 593px;
    box-sizing: border-box;
    overflow: hidden;
  }
  .card--front {
    left: 234px;
    width: 364px;
    background: var(--card-light);
    text-align: center;
    color: var(--text-dark);
  }
  .card--back {
    left: 628px;
    width: 367px;
    background: var(--card-green);
  }
  .card__backdrop {
    position: absolute;
    left: 20px;
    top: 0;
    width: 340px;
    height: 593px;
    background: radial-gradient(ellipse 45% 55% at 50% 50%, var(--card-green-soft) 0%, rgba(26, 92, 62, 0.45) 55%, rgba(6, 74, 46, 0) 100%);
  }
  .brand {
    position: absolute;
    left: 0;
    right: 0;
    display: flex;
    align-items: center;
    justify-content: center;
    gap: 10px;
    font-weight: 900;
    letter-spacing: 0.3px;
  }
  .brand__mark {
    width: 16px;
    height: 16px;
  }
  .card--front .brand {
    top: 200px;
    font-size: 26px;
    color: var(--brand-green);
  }
  .card--front .brand__mark { background: var(--brand-green); }
  .card--back .brand {
    top: 370px;
    font-size: 28px;
    color: var(--white);
  }
  .card--back .brand__mark { background: var(--white); }
  .person {
    position: absolute;
    top: 333px;
    left: 0;
    right: 0;
  }
  .person__name {
    margin: 0;
    font-size: 21px;
    line-height: 26px;
    font-weight: 400;
    color: var(--brand-green);
    letter-spacing: 0.3px;
  }
  .person__creds {
    font-size: 17px;
    color: var(--brand-brown);
  }
  .person__title {
    margin: 0;
    font-size: 17px;
    line-height: 22px;
  }
  .rule {
    width: 148px;
    height: 1px;
    background: var(--rule);
    margin: 9px auto 9px;
  }
  .rule--lower { margin: 7px auto 13px; }
  .address, .contact {
    margin: 0;
    font-size: 17px;
    line-height: 22px;
    font-style: normal;
  }
  .contact__label {
    font-weight: 700;
    color: var(--brand-green);
  }
</style>
</head>
<body>
<main class="canvas">
  <section class="card card--front" aria-label="Business card front">
    <div class="brand"><span class="brand__mark"></span>Verdon Ridgeworks</div>
    <div class="person">
      <h1 class="person__name">NEIL HASTOW, <span class="person__creds">CA, CPA</span></h1>
      <p class="person__title">Vice President Finance &amp;<br>Chief Financial Officer</p>
      <div class="rule"></div>
      <address class="address">840, 615 11 Street N.E.<br>Calgary, AB X9Q 4K1</address>
      <div class="rule rule--lower"></div>
      <p class="contact">
        <span class="contact__label">O:</span> (555)284-6071<br>
        <span class="contact__label">C:</span> (555)716-3342<br>
        <span class="contact__label">E:</span> nhastow@verdonridgeworks.example
      </p>
    </div>
  </section>
  <section class="card card--back" aria-label="Business card back">
    <div class="card__backdrop" role="img" aria-label="Large faint decorative brand backdrop in soft green tones"></div>
    <div class="brand"><span class="brand__mark"></span>Verdon Ridgeworks</div>
  </section>
</main>
</body>
</html>
```